Brightwave Travel and Tours

Hotel Reservations
Airline Ticketing
Day Tour

My business is a Travel agency. My services are issuing domestic and international tickets. Book room/hotel reservations local/international.
My color preference is apple green/orange/red/blue.
Images of beaches, tickets,luggage.

Industry/Entity Type

Business

```html
<!DOCTYPE html>
<html lang="en">
<head>
<meta charset="utf-8">
<title>Brightwave Travel and Tours – Business Card</title>
<link href="https://fonts.googleapis.com/css2?family=Open+Sans:wght@400;600&display=swap" rel="stylesheet">
<style>
  :root {
    --bg: #2b2b2b;
    --card: #1c1c1d;
    --card-edge: #111112;
    --accent: #1fa3dc;
    --accent-dark: #1a86b8;
    --text: #e9e9e9;
    --muted: #bfbfbf;
    --divider: #333335;
  }
  * { box-sizing: border-box; margin: 0; padding: 0; }
  html, body { width: 1200px; height: 900px; overflow: hidden; }
  body {
    background: var(--bg);
    font-family: "Open Sans", Arial, sans-serif;
    display: flex;
    align-items: center;
    justify-content: center;
    gap: 48px;
  }
  .card {
    width: 525px;
    height: 300px;
    background: var(--card);
    border-radius: 22px;
    position: relative;
    overflow: hidden;
    box-shadow: 0 0 0 1px var(--card-edge);
  }
  /* Info side */
  .card--info .brand-block {
    position: absolute;
    left: 30px;
    top: 60px;
    width: 170px;
    height: 150px;
    display: flex;
    flex-direction: column;
    align-items: center;
    justify-content: center;
    gap: 12px;
    text-align: center;
  }
  .brand-dot {
    width: 40px;
    height: 40px;
    border-radius: 50%;
    background: var(--accent);
  }
  .brand-name {
    color: var(--accent);
    font-weight: 600;
    font-size: 17px;
    line-height: 1.25;
  }
  .divider {
    position: absolute;
    left: 222px;
    top: 22px;
    width: 1px;
    height: 190px;
    background: var(--divider);
  }
  .contact {
    position: absolute;
    left: 246px;
    top: 26px;
    color: var(--text);
  }
  .contact__name {
    color: var(--accent);
    font-size: 19px;
    font-weight: 400;
    line-height: 1.2;
  }
  .contact__role {
    font-size: 13px;
    margin-bottom: 12px;
  }
  .contact__address {
    font-size: 13px;
    line-height: 1.35;
    margin-bottom: 12px;
  }
  .contact__list { list-style: none; font-size: 13px; line-height: 1.5; }
  .contact__list li { display: flex; align-items: center; gap: 8px; }
  .contact__list svg { width: 11px; height: 11px; flex: none; }
  .services {
    position: absolute;
    left: 0;
    right: 0;
    bottom: 30px;
    display: flex;
    justify-content: center;
    align-items: center;
    gap: 8px;
    color: var(--text);
    font-size: 15px;
  }
  .services__sep {
    width: 8px;
    height: 8px;
    border-radius: 50%;
    background: var(--accent);
  }
  /* Brand side */
  .card--brand {
    display: flex;
    flex-direction: column;
    align-items: center;
    justify-content: center;
    gap: 14px;
  }
  .card--brand .brand-dot { width: 56px; height: 56px; }
  .card--brand .brand-name { font-size: 26px; }
</style>
</head>
<body>
  <section class="card card--info" aria-label="Business card, contact side">
    <div class="brand-block">
      <span class="brand-dot"></span>
      <span class="brand-name">Brightwave Travel and Tours</span>
    </div>
    <div class="divider"></div>
    <div class="contact">
      <p class="contact__name">Marcus Hale</p>
      <p class="contact__role">Managing Director</p>
      <p class="contact__address">12345, Address Goes Here<br>Country Name, 123456.</p>
      <ul class="contact__list">
        <li>
          <svg viewBox="0 0 12 12" aria-hidden="true"><path fill="var(--accent)" d="M2 1h2.5l1 2.5-1.4 1a6 6 0 0 0 3.4 3.4l1-1.4L11 7.5V10a1 1 0 0 1-1 1A9 9 0 0 1 1 2a1 1 0 0 1 1-1z"/></svg>
          044-555 210 384
        </li>
        <li>
          <svg viewBox="0 0 12 12" aria-hidden="true"><rect x="0.5" y="2" width="11" height="8" rx="1" fill="var(--accent)"/><path d="M1 2.5l5 4 5-4" stroke="var(--card)" fill="none"/></svg>
          info@brightwavetrips.com
        </li>
        <li>
          <svg viewBox="0 0 12 12" aria-hidden="true"><circle cx="6" cy="6" r="5" fill="none" stroke="var(--accent)" stroke-width="1.4"/><path d="M1 6h10M6 1c-2.5 3-2.5 7 0 10M6 1c2.5 3 2.5 7 0 10" stroke="var(--accent)" fill="none"/></svg>
          www.brightwavetrips.com
        </li>
      </ul>
    </div>
    <div class="services">
      <span>Hotel Reservations</span>
      <span class="services__sep"></span>
      <span>Airline Ticketing</span>
      <span class="services__sep"></span>
      <span>Day Tour</span>
    </div>
  </section>

  <section class="card card--brand" aria-label="Business card, brand side">
    <span class="brand-dot"></span>
    <span class="brand-name">Brightwave Travel and Tours</span>
  </section>
</body>
</html>
```